KWCA '13 Presentation Dinner

Harrowfield Junior Hoops Circle Inc., or KWCA for short is a local basketball league based in Brisbane Southside, Australia.
We're holding our annual award presentation night and would like to advertise to our 350+ members via posters around the basketball hall and local shopping centres. Majority of our members are in aged 21-30.
The presentation dinner is held at a local Chinese restaurant with lucky door prize, raffles, trivia, '13 highlight video and presentation of '13 awards.
Essential Details are:
Location: Goldwillow Restaurant, 4/682 Fenner Rd, Sunnybank
Date: Saturday November 23rd 2013
Time: 6:00PM
Dress Code: Formal
See KWCA staff for more details
Optional Detail:
Cost: $400 per table of 10
Discount: Register before 14th September to receive $50 off - $350 per table
The final design should indicate this will be a fun night aimed at young adults and should not be missed by KWCA members.

```html
<!DOCTYPE html>
<html lang="en">
<head>
<meta charset="utf-8">
<title>KWCA Annual Award Presentation Night</title>
<link href="https://fonts.googleapis.com/css2?family=Graduate&display=swap" rel="stylesheet">
<style>
  :root {
    --festive-red: #b0001e;
    --cream: #f7f0c6;
    --soft-red: #c42a3e;
  }
  html, body {
    margin: 0;
    padding: 0;
    width: 848px;
    height: 1200px;
    overflow: hidden;
    background: var(--festive-red);
  }
  .poster {
    position: relative;
    width: 848px;
    height: 1200px;
    background: var(--festive-red);
    color: var(--cream);
    font-family: "Graduate", serif;
    text-transform: uppercase;
    overflow: hidden;
  }
  .frame-lines, .corner-ornament, .gate-roof, .gate-pillar, .league-mark {
    position: absolute;
  }
  .frame-lines { left: 0; top: 0; }
  .corner-ornament {
    width: 118px;
    height: 118px;
    background: var(--soft-red);
    border: 3px solid var(--cream);
    box-sizing: border-box;
  }
  .corner-ornament.top-left { left: 30px; top: 30px; }
  .corner-ornament.top-right { right: 30px; top: 30px; }
  .corner-ornament.bottom-left { left: 30px; bottom: 30px; }
  .corner-ornament.bottom-right { right: 30px; bottom: 30px; }

  .league-mark {
    left: 329px;
    top: 103px;
    width: 190px;
    height: 190px;
    border-radius: 50%;
    background: var(--cream);
    display: flex;
    align-items: center;
    justify-content: center;
    color: var(--festive-red);
    font-size: 40px;
    letter-spacing: 4px;
  }
  .centered {
    position: absolute;
    left: 0;
    width: 100%;
    text-align: center;
    margin: 0;
    line-height: 1;
    font-weight: 400;
    white-space: nowrap;
  }
  .league-name { top: 305px; font-size: 31px; letter-spacing: 1px; }
  .title-rule {
    position: absolute;
    left: 72px;
    width: 704px;
    height: 0;
    border-top: 2px solid var(--cream);
  }
  .title-rule.upper { top: 343px; }
  .title-rule.lower { top: 347px; }
  .event-name { top: 355px; font-size: 34px; letter-spacing: 1px; }

  .gate-roof {
    left: 103px;
    top: 417px;
    width: 647px;
    height: 121px;
    background: var(--cream);
  }
  .gate-sign {
    top: 491px;
    font-size: 30px;
    letter-spacing: 10px;
    color: var(--festive-red);
  }
  .gate-pillar {
    top: 557px;
    width: 31px;
    height: 471px;
    background: var(--cream);
  }
  .gate-pillar.left { left: 173px; }
  .gate-pillar.right { left: 647px; }

  .venue-name { top: 585px; font-size: 50px; }
  .venue-kind { top: 646px; font-size: 25px; letter-spacing: 12px; }
  .venue-address { top: 680px; font-size: 18px; }
  .event-day { top: 737px; font-size: 68px; }
  .event-date { top: 806px; font-size: 28px; }
  .event-time { top: 873px; font-size: 69px; }
  .dress-code { top: 953px; font-size: 25px; }
  .more-details { top: 1045px; font-size: 14px; }
</style>
</head>
<body>
<main class="poster">
  <svg class="frame-lines" width="848" height="1200" viewBox="0 0 848 1200" aria-hidden="true">
    <g fill="none" stroke="var(--cream)" stroke-width="3">
      <rect x="30" y="30" width="788" height="1140"/>
      <rect x="44" y="44" width="760" height="1112"/>
    </g>
  </svg>
  <div class="corner-ornament top-left" role="img" aria-label="Lattice corner ornament"></div>
  <div class="corner-ornament top-right" role="img" aria-label="Lattice corner ornament"></div>
  <div class="corner-ornament bottom-left" role="img" aria-label="Lattice corner ornament"></div>
  <div class="corner-ornament bottom-right" role="img" aria-label="Lattice corner ornament"></div>

  <div class="league-mark">KWCA</div>

  <h2 class="centered league-name">Harrowfield Junior Hoops Circle Inc</h2>
  <div class="title-rule upper"></div>
  <div class="title-rule lower"></div>
  <h1 class="centered event-name">Annual Award Presentation Night</h1>

  <div class="gate-roof" role="img" aria-label="Chinese gate roof illustration"></div>
  <p class="centered gate-sign">KWCA</p>
  <div class="gate-pillar left" role="img" aria-label="Patterned gate pillar"></div>
  <div class="gate-pillar right" role="img" aria-label="Patterned gate pillar"></div>

  <p class="centered venue-name">Goldwillow</p>
  <p class="centered venue-kind">Restaurant</p>
  <p class="centered venue-address">4/682 Fenner Rd, Sunnybank</p>

  <p class="centered event-day">Saturday</p>
  <p class="centered event-date">November 23rd – 2013</p>

  <p class="centered event-time">6:00 PM</p>
  <p class="centered dress-code">Dress Code: Formal</p>

  <p class="centered more-details">See KWCA staff for more details</p>
</main>
</body>
</html>
```